Digital Billboard to Drive Buying Local

We are a Montana-based soap and hygiene product company (think Dr. Bramble and Solace). We are looking to design a billboard ad for some digital billboards around Montana. We will have 8 seconds at a time to make an impression so we need a quick and to the point ad. We are thinking a line like "Bring Montana inside. Pine Hush, Natural Soap." (Pine Hush is the name of one of our soaps and is also the unofficial slogan for Montana.) Our products are made in Montana and we want to appeal to both people that appreciate that as well as outdoors lovers. I'll attach a picture of the soap box, our logo, website and a couple of examples of billboards from companies like Baron Flint and Ploughboy Ned. Let me know if you need higher-resolution images.
Website: BirchEmberCo.com
Company Name: Birch Ember Co.

```html
<!DOCTYPE html>
<html lang="en">
<head>
<meta charset="utf-8">
<title>Birch Ember Co. — Billboard</title>
<link rel="stylesheet" href="https://fonts.googleapis.com/css2?family=Oswald:wght@200;600&family=Montserrat:wght@800&family=Poppins:wght@700&display=swap">
<style>
  :root {
    --stage: #5f9068;
    --sky-top: #1f4f6e;
    --sky-mid: #5d7f8f;
    --hills: #2f5a2c;
    --hills-dark: #1f3d20;
    --ground: #4a3f2c;
    --white: #ffffff;
    --leaf: #c8f0a6;
    --pill: #8fc35f;
    --ink: #13301c;
    --kraft: #c79a4c;
  }
  * { margin: 0; padding: 0; box-sizing: border-box; }
  html, body { width: 901px; height: 1200px; overflow: hidden; }
  body { background: var(--stage); position: relative; }

  .billboard {
    position: absolute;
    left: 20px; top: 385px;
    width: 861px; height: 430px;
    overflow: hidden;
    box-shadow: 0 10px 24px rgba(0,0,0,.35);
  }
  .billboard__scenery {
    position: absolute; inset: 0;
    background: linear-gradient(180deg, var(--sky-top) 0%, var(--sky-mid) 20%, #3d6a52 36%, var(--hills) 60%, var(--hills-dark) 84%, var(--ground) 100%);
  }
  .billboard__product {
    position: absolute;
    left: 308px; top: 126px;
    width: 232px; height: 215px;
    border-radius: 3px;
    background: linear-gradient(135deg, var(--kraft) 0%, #b88a3e 55%, #7fa7a4 100%);
  }

  .headline-left {
    position: absolute;
    left: 39px; top: 32px;
    font-family: 'Oswald', sans-serif;
    color: var(--white);
    text-transform: uppercase;
    line-height: .98;
    font-size: 70px;
    letter-spacing: -2px;
  }
  .headline-left__lead { font-weight: 200; display: block; }
  .headline-left__main { font-weight: 600; display: block; }

  .site-pill {
    position: absolute;
    left: 39px; top: 253px;
    width: 273px; height: 42px;
    border-radius: 21px;
    background: var(--pill);
    font-family: 'Poppins', sans-serif;
    font-weight: 700;
    font-size: 21px;
    color: var(--ink);
    display: flex; align-items: center;
    padding-left: 14px;
  }

  .brand-name {
    position: absolute;
    left: 330px; top: 86px;
    width: 200px;
    text-align: center;
    font-family: 'Oswald', sans-serif;
    font-weight: 200;
    font-size: 17px;
    letter-spacing: 2.5px;
    color: var(--white);
    text-transform: uppercase;
  }

  .headline-right {
    position: absolute;
    left: 561px; top: 30px;
    font-family: 'Montserrat', sans-serif;
    font-weight: 800;
    text-transform: uppercase;
    white-space: nowrap;
  }
  .headline-right__product {
    display: block;
    font-size: 92px;
    line-height: 85px;
    letter-spacing: -3px;
    color: var(--leaf);
  }
  .headline-right__category {
    display: block;
    font-size: 50px;
    line-height: 46px;
    letter-spacing: -1px;
    color: var(--white);
  }
  .headline-right__product + .headline-right__category { margin-top: 4px; }
</style>
</head>
<body>
  <section class="billboard" aria-label="Birch Ember Co. billboard">
    <div class="billboard__scenery" role="img" aria-label="Photograph of green forested Montana mountain ridges under a cloudy blue sky, with a mossy tree stump on a wooden surface in front"></div>
    <div class="billboard__product" role="img" aria-label="Photograph of a green bar of soap in front of its kraft paper box"></div>

    <h1 class="headline-left">
      <span class="headline-left__lead">Bring</span>
      <span class="headline-left__main">Montana</span>
      <span class="headline-left__main">Inside.</span>
    </h1>

    <div class="site-pill">BirchEmberCo.com</div>

    <div class="brand-name">Birch Ember Co.</div>

    <h2 class="headline-right">
      <span class="headline-right__product">Pine</span>
      <span class="headline-right__product">Hush</span>
      <span class="headline-right__category">Natural</span>
      <span class="headline-right__category">Soap</span>
    </h2>
  </section>
</body>
</html>
```